Award winning R&B Male Vocalist from Philadelphia,Pa needs CD Art Work

On my last CD I used a Photo of myself. I want to go in an entirely different direction this time. Maybe a piano or some musical instruments or a vintage microphone in some sort abstract design. Very classy not too much...
The title of the album is "Velvet dawn." This is my third album, so I'm thinking something along the lines of Corbin's Driftwood cover, but not a rip off!!!
Woke up this morning and in my head I saw a white baby grand piano sitting in a brightly lit room, with red, and other flowers all around, and on the piano, a photo in a beautiful frame that you can barely make out of a happy couple. I have uploaded the photo to use.

Target Market(s)

35 to 60 year old men and women

Industry/Entity Type

Work

Font styles to use
Decorative
Script

Requirements
Must have
• My name "Lusko" and the name of the album. "Velvet dawn"
Nice to have
• Lay out the uploaded photo on the inside tray
Should not have
• Any reference to Sex or violence!!!

```html
<!DOCTYPE html>
<html lang="en">
<head>
<meta charset="utf-8">
<title>Lusko – Velvet Dawn</title>
<link href="https://fonts.googleapis.com/css2?family=Rye&display=swap" rel="stylesheet">
<style>
  :root {
    --backdrop: #e6e1cf;
    --wood-dark: #2a1209;
    --wood-mid: #5a2d14;
    --key-shadow: #3b2a1c;
    --key-warm: #a57a45;
    --key-light: #d8b47c;
    --type-white: #fbf8f2;
  }
  html, body {
    margin: 0;
    padding: 0;
    width: 1200px;
    height: 840px;
    overflow: hidden;
    background: var(--backdrop);
  }
  .canvas {
    position: relative;
    width: 1200px;
    height: 840px;
    display: flex;
    align-items: center;
    justify-content: center;
  }
  .album-cover {
    position: relative;
    width: 720px;
    height: 720px;
    overflow: hidden;
    box-shadow: 0 10px 30px rgba(60, 45, 20, 0.25);
  }
  .cover-photo {
    position: absolute;
    inset: 0;
    background:
      linear-gradient(160deg, rgba(0,0,0,0) 55%, rgba(30,15,5,0.35) 100%),
      linear-gradient(150deg,
        var(--wood-dark) 0%,
        var(--wood-mid) 18%,
        var(--key-light) 30%,
        var(--key-shadow) 40%,
        var(--key-warm) 55%,
        var(--key-light) 68%,
        var(--key-warm) 80%,
        var(--key-shadow) 100%);
    filter: blur(2px);
  }
  .cover-title {
    position: absolute;
    left: 0;
    right: 0;
    top: 33%;
    text-align: center;
    color: var(--type-white);
    font-family: "Rye", serif;
    line-height: 1;
  }
  .artist-name {
    display: block;
    font-size: 150px;
    letter-spacing: 2px;
    transform: translateX(-30px);
  }
  .album-name {
    display: block;
    margin-top: 10px;
    font-size: 72px;
    letter-spacing: 1px;
    text-transform: uppercase;
  }
</style>
</head>
<body>
  <main class="canvas">
    <section class="album-cover">
      <div class="cover-photo" role="img" aria-label="Close-up photograph of piano keys in warm brown and ivory tones, softly out of focus"></div>
      <h1 class="cover-title">
        <span class="artist-name">LUSKO</span>
        <span class="album-name">Velvet Dawn</span>
      </h1>
    </section>
  </main>
</body>
</html>
```